Business Card and Simple Logo Desgin

New Zealand based start up company "Brook Advisory LTD" requires business cards and simple logo design.

Card Content.

Brook Advisory LTD

Joanna Pritchard
CA, BMS (Hons)

j.pritchard@brookadvisory.co.nz
PH +64 21 574 160

Target Market(s)

Corporate Business in IT, Finance and accounting.

Industry/Entity Type

Business

```html
<!DOCTYPE html>
<html lang="en">
<head>
<meta charset="utf-8">
<title>Brook Advisory LTD — Business Card</title>
<link rel="stylesheet" href="https://fonts.googleapis.com/css2?family=Source+Sans+3:wght@400;600&display=swap">
<style>
  :root {
    --backdrop: #1c1c1e;
    --card-dark: #15181b;
    --card-mid: #2c3136;
    --card-sheen: #3a4046;
    --text-light: #e9ecee;
    --text-soft: #c9cdd0;
    --brand-gold: #d9b24a;
    --ring-copper: #b9733a;
    --bar-silver-dark: #8e9398;
    --bar-silver-light: #f4f5f6;
  }

  * { margin: 0; padding: 0; box-sizing: border-box; }

  html, body {
    width: 1200px;
    height: 900px;
    overflow: hidden;
    background: var(--backdrop);
    font-family: "Source Sans 3", "Myriad Pro", Arial, sans-serif;
  }

  .canvas {
    position: relative;
    width: 1200px;
    height: 900px;
    display: flex;
    align-items: center;
    justify-content: center;
  }

  .business-card {
    position: relative;
    width: 900px;
    height: 550px;
    border-radius: 22px;
    background:
      linear-gradient(118deg, transparent 30%, rgba(255,255,255,0.07) 42%, transparent 55%),
      linear-gradient(160deg, var(--card-sheen) 0%, var(--card-mid) 30%, var(--card-dark) 100%);
    box-shadow: 0 20px 50px rgba(0,0,0,0.55);
    color: var(--text-light);
    overflow: hidden;
  }

  .brand-mark {
    position: absolute;
    left: 62px;
    top: 70px;
    width: 170px;
    height: 170px;
  }

  .brand-name {
    position: absolute;
    left: 262px;
    top: 86px;
    font-size: 46px;
    font-weight: 600;
    letter-spacing: 0.2px;
    color: var(--brand-gold);
    white-space: nowrap;
  }

  .brand-bar {
    position: absolute;
    left: 262px;
    top: 150px;
    width: 600px;
    height: 22px;
    border-radius: 11px;
    background: linear-gradient(90deg, var(--bar-silver-light) 0%, var(--bar-silver-dark) 22%, var(--bar-silver-light) 55%, var(--bar-silver-dark) 80%, var(--bar-silver-light) 100%);
    box-shadow: inset 0 -2px 3px rgba(0,0,0,0.25);
  }

  .contact-block {
    position: absolute;
    right: 40px;
    top: 205px;
    text-align: right;
  }

  .person-name {
    font-size: 44px;
    font-weight: 400;
    color: var(--text-light);
    line-height: 1.1;
  }

  .person-credentials {
    font-size: 26px;
    color: var(--text-soft);
    margin-top: 6px;
  }

  .person-phone {
    font-size: 28px;
    color: var(--text-soft);
    margin-top: 46px;
  }

  .person-email {
    font-size: 31px;
    color: var(--text-light);
    margin-top: 6px;
  }
</style>
</head>
<body>
<main class="canvas">
  <article class="business-card">
    <svg class="brand-mark" viewBox="0 0 170 170" aria-hidden="true">
      <circle cx="85" cy="85" r="78" fill="var(--card-dark)" stroke="var(--ring-copper)" stroke-width="10"/>
    </svg>
    <h1 class="brand-name">Brook Advisory LTD</h1>
    <div class="brand-bar"></div>
    <section class="contact-block">
      <p class="person-name">Joanna Pritchard</p>
      <p class="person-credentials">CA, BMS (Hons)</p>
      <p class="person-phone">PH +64 21 574 160</p>
      <p class="person-email">j.pritchard@brookadvisory.co.nz</p>
    </section>
  </article>
</main>
</body>
</html>
```